Denim Retailer needs advert for sale

We need a advertisement designed that can be used to market our upcoming promotion through our electronic media channels which include Facebook, email & website.

Promotion Details:

Title: Pick A Pair Sale
Offer: Buy 1 pair =10% off, Buy 2 pairs = 15% off, Buy 3+ pairs = 20% off.

Our main brands are Tavon's, Gallop by Orn & Cobbleton for both men and women.

Our Target market is 25-55 yo male & female.

I would ideally like an eye catching design that encapsulates premise of our promotion. I don't have any specific theme or colour scheme, bust must be gender neutral.

Target Market(s)

25-55 male & female

Industry/Entity Type

Electronic

Requirements
Must have
• Must be sized to accommodate a Facebook post.

```html
<!DOCTYPE html>
<html lang="en">
<head>
<meta charset="utf-8">
<title>Pick A Pair Sale</title>
<link rel="stylesheet" href="https://fonts.googleapis.com/css2?family=Baloo+2:wght@800&family=Caladea&family=Open+Sans:wght@600&display=swap">
<style>
  :root {
    --asphalt-dark: #2b2c2a;
    --asphalt-mid: #5b5d58;
    --asphalt-light: #8d918a;
    --asphalt-cool: #a9b3ab;
    --sun-yellow: #f6a81c;
    --tang-orange: #f26b38;
    --white: #ffffff;
    --ink: #141414;
  }
  html, body {
    margin: 0;
    padding: 0;
    overflow: hidden;
    background: var(--ink);
  }
  .advert {
    position: relative;
    width: 987px;
    height: 1200px;
    overflow: hidden;
  }
  .scene-photo {
    position: absolute;
    inset: 0;
    background:
      radial-gradient(ellipse at 85% 40%, rgba(120,140,150,0.35), transparent 55%),
      linear-gradient(180deg, var(--asphalt-dark) 0%, var(--asphalt-mid) 35%, var(--asphalt-light) 75%, var(--asphalt-cool) 100%);
  }
  .headline {
    position: absolute;
    left: 99px;
    top: 150px;
    margin: 0;
    display: flex;
    align-items: baseline;
    gap: 22px;
    white-space: nowrap;
  }
  .headline-pick {
    font-family: "Baloo 2", "Arial Rounded MT Bold", sans-serif;
    font-weight: 800;
    font-size: 128px;
    line-height: 1;
    letter-spacing: -3px;
  }
  .headline-pick .yellow { color: var(--sun-yellow); }
  .headline-pick .orange { color: var(--tang-orange); }
  .headline-sale {
    font-family: "Open Sans", sans-serif;
    font-weight: 600;
    font-size: 74px;
    color: var(--white);
    letter-spacing: -1px;
  }
  .offer-list {
    position: absolute;
    left: 113px;
    top: 420px;
    margin: 0;
    padding: 0;
    list-style: none;
    font-family: "Caladea", "Cambria", serif;
    font-size: 44px;
    color: var(--white);
  }
  .offer-list li {
    height: 100px;
    line-height: 60px;
  }
  .brand-mark {
    position: absolute;
    left: 103px;
    top: 990px;
    display: flex;
    align-items: center;
    gap: 18px;
    font-family: "Open Sans", sans-serif;
    font-weight: 600;
    font-size: 56px;
    color: var(--white);
  }
  .brand-mark .square {
    width: 40px;
    height: 40px;
    background: var(--white);
  }
</style>
</head>
<body>
  <main class="advert">
    <div class="scene-photo" role="img" aria-label="Photo of a skateboarder's jean-clad leg and sneaker resting on a tilted skateboard on asphalt"></div>

    <h1 class="headline">
      <span class="headline-pick"><span class="yellow">Pick </span><span class="orange">A </span><span class="yellow">Pair</span></span>
      <span class="headline-sale">Sale</span>
    </h1>

    <ul class="offer-list">
      <li>Buy 1 pair =10% off</li>
      <li>Buy 2 pairs = 15% off</li>
      <li>Buy 3+ pairs = 20% off.</li>
    </ul>

    <div class="brand-mark">
      <span class="square" aria-hidden="true"></span>
      <span class="brand-name">Gallop by Orn</span>
    </div>
  </main>
</body>
</html>
```